Speisekarten-Design für Gastronomiebetrieb
Zielgruppe
Wir sind ein Gastronomiebetrieb in einer Studentenstadt. Unsere Hauptzielgruppe sind junge Menschen und Studenten, aber auch älteres Puplikum. Wir möchten gerne ein neues Speisekartendesign, da unser aktuelles seit über 10 Jahren sich kaum verändert hat.
Aufgabenstellung
Gerne könne Sie sich die aktulle Speisekarte auf der unserer Hompeage anschauen: www.tomello-kassel.de
Auf der Frontseite soll die Farbrichtung Orange und natürlich das Logo beibehalten werden. Für die restlichen Seiten gibt es diese Einschränkung nicht. Uns ist wichtig, dass die Speisekarte modern, bunt und peppig ist. Das heisst möglichst mit kräftigen Farben und Bildern von Speisen und Getränken arbeiten.

```html
<!DOCTYPE html>
<html lang="de">
<head>
<meta charset="utf-8">
<title>Tomello – Frühstück, Kaffee und Tee</title>
<link rel="stylesheet" href="https://fonts.googleapis.com/css2?family=Open+Sans:wght@400;700&family=Permanent+Marker&display=swap">
<style>
  :root {
    --bg: #111111;
    --orange: #ff8a00;
    --orange-dark: #c86a00;
    --body-font: "Open Sans", "Segoe UI", sans-serif;
    --brush-font: "Permanent Marker", cursive;
  }
  * { box-sizing: border-box; margin: 0; padding: 0; }
  html, body { width: 720px; height: 1200px; overflow: hidden; background: var(--bg); }
  .menu {
    position: relative; width: 720px; height: 1200px;
    background: var(--bg); color: var(--orange);
    font-family: var(--body-font);
  }
  .corner { position: absolute; border-color: var(--orange); border-style: solid; border-width: 0; }
  .corner--top-left { left: 43px; top: 43px; width: 146px; height: 91px; border-top-width: 6px; border-left-width: 6px; }
  .corner--top-right { left: 531px; top: 43px; width: 146px; height: 146px; border-top-width: 6px; border-right-width: 6px; }
  .corner--bottom { left: 43px; top: 1145px; width: 634px; height: 12px; border-bottom-width: 6px; border-left-width: 6px; border-right-width: 6px; }

  .brand {
    position: absolute; left: 264px; top: 22px; width: 190px; height: 56px;
    display: flex; align-items: center; gap: 10px;
  }
  .brand__dot { width: 40px; height: 40px; border-radius: 50%; background: var(--orange); }
  .brand__name { font-size: 34px; font-weight: 700; color: var(--orange); line-height: 1; }

  .cup-art {
    position: absolute; left: 451px; top: 72px; width: 146px; height: 126px;
    border-radius: 12px;
    background: radial-gradient(ellipse at 50% 60%, var(--orange) 0%, var(--orange-dark) 55%, var(--bg) 80%);
  }

  .heading {
    position: absolute; font-family: var(--brush-font); color: var(--orange);
    font-size: 40px; line-height: 1; white-space: nowrap;
  }
  .heading--breakfast { left: 115px; top: 110px; }
  .heading--drinks { left: 386px; top: 776px; font-size: 38px; }

  .dish { position: absolute; width: 287px; }
  .dish__head { display: flex; justify-content: space-between; font-size: 17.5px; line-height: 20px; white-space: nowrap; }
  .dish__num { margin-right: 8px; }
  .dish__desc { font-size: 12.4px; line-height: 16.2px; margin-top: 1px; }
  .col-left { left: 62px; }
  .col-right { left: 371px; }

  .hours-box {
    position: absolute; left: 43px; top: 553px; width: 634px; height: 181px;
    border: 6px solid var(--orange);
    text-align: center; font-size: 18.5px; line-height: 23px;
    padding-top: 42px;
  }
  .hours-box strong { font-weight: 700; }
  .hours-box__note { margin-top: 21px; }

  .drink-list { position: absolute; list-style: none; }
  .drink-list li { display: flex; justify-content: space-between; font-size: 18.5px; height: 38.6px; line-height: 22px; }
  .drink-list--coffee { left: 78px; top: 774px; width: 271px; }
  .drink-list--tea { left: 386px; top: 851px; width: 272px; }
</style>
</head>
<body>
<main class="menu">
  <div class="corner corner--top-left"></div>
  <div class="corner corner--top-right"></div>
  <div class="corner corner--bottom"></div>

  <header class="brand">
    <span class="brand__dot"></span>
    <span class="brand__name">Tomello</span>
  </header>

  <div class="cup-art" role="img" aria-label="Illustration einer dampfenden Kaffeetasse auf Untertasse"></div>

  <h1 class="heading heading--breakfast">Frühstück:</h1>

  <section class="dish col-left" style="top:176px">
    <div class="dish__head"><span><span class="dish__num">(1)</span>Kleines Frühstück</span><span>4,50€</span></div>
    <p class="dish__desc">1 Vollkornbrötchen, Butter und Marmelade</p>
  </section>
  <section class="dish col-left" style="top:231px">
    <div class="dish__head"><span><span class="dish__num">(2)</span>Großes Frühstück</span><span>6,90€</span></div>
    <p class="dish__desc">2 Brötchen, Butter, Marmelade, Schinken, Käse, Salami, 1 Ei und 1 Milchkaffee</p>
  </section>
  <section class="dish col-left" style="top:302px">
    <div class="dish__head"><span><span class="dish__num">(3)</span>Französisches Frühstück</span><span>7,10€</span></div>
    <p class="dish__desc">2 Brötchen, 1 Croissant, Butter, Marmelade, Honig, Nocciola, Käse, Salami und 1 Glas O-Saft</p>
  </section>
  <section class="dish col-left" style="top:373px">
    <div class="dish__head"><span><span class="dish__num">(4)</span>Frühstück Tomello</span><span>7,50€</span></div>
    <p class="dish__desc">1 Vollkornbrötchen, 1 Croissant, Butter, Marmelade, 1 Spiegelei, Schinken, Käse, Salami und ein Glas O-Saft</p>
  </section>
  <section class="dish col-left" style="top:460px">
    <div class="dish__head"><span><span class="dish__num">(5)</span>Frühstück Kassel</span><span>7,50€</span></div>
    <p class="dish__desc">2 Brötchen, Butter, Marmelade, 3 Rühreier, Schinken, Tomaten und 1 Milchkaffe</p>
  </section>

  <section class="dish col-right" style="top:231px">
    <div class="dish__head"><span><span class="dish__num">(6)</span>Großes Frühstück</span><span>6,90€</span></div>
    <p class="dish__desc">2 Brötchen, Butter, Marmelade, Schinken, Käse, Salami, 1 Ei und 1 Milchkaffee</p>
  </section>
  <section class="dish col-right" style="top:302px">
    <div class="dish__head"><span><span class="dish__num">(7)</span>Französisches Frühstück</span><span>7,10€</span></div>
    <p class="dish__desc">2 Brötchen, 1 Croissant, Butter, Marmelade, Honig, Nocciola, Käse, Salami und 1 Glas O-Saft</p>
  </section>
  <section class="dish col-right" style="top:373px">
    <div class="dish__head"><span><span class="dish__num">(8)</span>Frühstück Tomello</span><span>7,50€</span></div>
    <p class="dish__desc">1 Vollkornbrötchen, 1 Croissant, Butter, Marmelade, 1 Spiegelei, Schinken, Käse, Salami und ein Glas O-Saft</p>
  </section>
  <section class="dish col-right" style="top:460px">
    <div class="dish__head"><span><span class="dish__num">(9)</span>Frühstück Kassel</span><span>7,50€</span></div>
    <p class="dish__desc">2 Brötchen, Butter, Marmelade, 3 Rühreier, Schinken, Tomaten und 1 Milchkaffe</p>
  </section>

  <section class="hours-box">
    <p>Montag bis Donnerstag von <strong>10:00</strong> bis <strong>13:00 Uhr</strong></p>
    <p>Freitag &amp; Samstag von <strong>10:00</strong> bis <strong>15:00 Uhr</strong></p>
    <p class="hours-box__note">Zu jedem Frühstück gibt es Kaffee und Tee, soviel Sie möchten</p>
  </section>

  <ul class="drink-list drink-list--coffee">
    <li><span>Espresso</span><span>1,90€</span></li>
    <li><span>Caffee Crema</span><span>2,10€</span></li>
    <li><span>Großer Caffee Crema</span><span>2,60€</span></li>
    <li><span>Doppelter Espresso</span><span>2,60€</span></li>
    <li><span>Cappuccino</span><span>2,50€</span></li>
    <li><span>Caffee Latte (Milchkaffe)</span><span>2,90€</span></li>
    <li><span>Latte Macchiato</span><span>2,90€</span></li>
    <li><span>Kaffee</span><span>2,10€</span></li>
    <li><span>Mehr-Kaffe</span><span>1,90€</span></li>
  </ul>

  <h2 class="heading heading--drinks">Kaffee und Tee:</h2>

  <ul class="drink-list drink-list--tea">
    <li><span>Beispiel-Tee</span><span>1,90€</span></li>
    <li><span>Caffee-Tee</span><span>2,10€</span></li>
    <li><span>Lecker-Tee</span><span>2,60€</span></li>
    <li><span>Mehr-Tee</span><span>2,60€</span></li>
    <li><span>Schwarzer-Tee</span><span>2,50€</span></li>
    <li><span>Blauer-Tee</span><span>2,90€</span></li>
    <li><span>Noch-Tee</span><span>2,90€</span></li>
  </ul>
</main>
</body>
</html>
```